Solar appointment reminder card

We are looking for a new design for our appointment reminder card since we have changed our logo. The card should have the new logo along with space for the employee to hand write the customers appointment date, time, the employees name and phone number.
I've uploaded what our old basic appointment card looked like and our new logo.

The cards should be in a standard business card size and could be horizontal or vertical.

```html
<!DOCTYPE html>
<html lang="en">
<head>
<meta charset="utf-8">
<title>Sunline Appointment Card</title>
<link rel="stylesheet" href="https://fonts.googleapis.com/css2?family=Roboto:wght@700&family=Signika:wght@500&display=swap">
<style>
  :root {
    --backdrop: #fcc72a;
    --card-black: #000000;
    --card-white: #ffffff;
    --label-yellow: #fdd22b;
    --brand-orange: #f7941d;
    --brand-sun: #fbc21b;
    --rule-grey: #555555;
  }
  * { margin: 0; padding: 0; box-sizing: border-box; }
  html, body { width: 1200px; height: 1200px; overflow: hidden; }
  body { background: var(--backdrop); position: relative; font-family: "Signika", sans-serif; }

  .card {
    position: absolute; left: 322px; top: 100px;
    width: 556px; height: 1000px;
    background: var(--card-white);
    box-shadow: 0 10px 30px rgba(0,0,0,0.25);
    overflow: hidden;
  }
  .card-header {
    position: absolute; left: 0; top: 0; width: 100%; height: 418px;
    background: var(--card-black);
  }
  .brand {
    position: absolute; left: 0; top: 110px; width: 100%;
    display: flex; align-items: center; justify-content: center; gap: 22px;
  }
  .brand-dot {
    width: 70px; height: 70px; border-radius: 50%;
    background: var(--brand-sun);
  }
  .brand-name {
    font-family: "Signika", sans-serif; font-weight: 500;
    font-size: 78px; letter-spacing: 2px;
    color: var(--brand-orange);
  }
  .header-rule {
    position: absolute; left: 36px; top: 309px; width: 484px; height: 3px;
    background: linear-gradient(90deg, rgba(120,120,120,0), #8a8a8a 50%, rgba(120,120,120,0));
  }
  .card-title {
    position: absolute; left: 0; top: 328px; width: 100%;
    text-align: center;
    font-family: "Roboto", sans-serif; font-weight: 700;
    font-size: 56px; color: var(--card-white);
  }

  .field-bar {
    position: absolute; left: 0; width: 100%; height: 41px;
    background: var(--card-black);
  }
  .field-bar::after {
    content: ""; position: absolute; left: 50px; top: 41px;
    border-left: 7px solid transparent; border-right: 7px solid transparent;
    border-top: 8px solid var(--card-black);
  }
  .field-label {
    position: absolute; left: 42px; top: 4px;
    font-size: 29px; letter-spacing: 0.5px; color: var(--label-yellow);
  }
  .write-line {
    position: absolute; left: 42px; width: 462px; height: 2px;
    background: var(--rule-grey);
  }
  .meridiem {
    position: absolute; right: 52px;
    font-size: 26px; color: #222;
  }
</style>
</head>
<body>
  <div class="card">
    <div class="card-header">
      <div class="brand">
        <span class="brand-dot"></span>
        <span class="brand-name">SUNLINE</span>
      </div>
      <div class="header-rule"></div>
      <div class="card-title">Appoinment</div>
    </div>

    <div class="field-bar" style="top:455px"><span class="field-label">Date</span></div>
    <div class="write-line" style="top:568px"></div>

    <div class="field-bar" style="top:580px"><span class="field-label">Time</span></div>
    <div class="meridiem" style="top:660px">a.m. / p.m.</div>
    <div class="write-line" style="top:696px"></div>

    <div class="field-bar" style="top:706px"><span class="field-label">Employees name</span></div>
    <div class="write-line" style="top:821px"></div>

    <div class="field-bar" style="top:833px"><span class="field-label">Phone number</span></div>
    <div class="write-line" style="top:957px"></div>
  </div>
</body>
</html>
```